Dravetti Business Cards

We need a business card design for Dravetti Mining.

This is a B2B company that buys and sells large machinery tires within the coal mining industry. The design should the strong, crisp and masculine. I have uploaded the company logo and rough mock-up of what the back of the card should look like. the front of the card should have the same look/feel as the back. I need editable templates for both the front and the back of the card.

Color scheme should be grey/green/black

Contact information to include on the card:
Name: Owen Pellsworth
Title: Managing Director
Phone: 972-555-0143
Address: 3157 Brantley #5 Dallas, TX 75209
Email: Owen@Dravetti-example.com

I am also opening a contest for letterhead design. If you submit a business card design, please also submit a letterhead design with the same look/feel. The winner of the business card design will also will the letter head and be paid for both.

Target Market(s)

Procurement men/women in the coal mining industry

Industry/Entity Type

Coal Mining

```html
<!DOCTYPE html>
<html lang="en">
<head>
<meta charset="utf-8">
<title>Dravetti Business Cards</title>
<link rel="stylesheet" href="https://fonts.googleapis.com/css2?family=Saira:wght@400;600;700&display=swap">
<style>
  :root {
    --stage: #d6d6d6;
    --stage-edge: #9a9a9a;
    --card: #161616;
    --card-deep: #0c0c0c;
    --green: #6cc01f;
    --white: #f4f4f4;
    --muted: #cfcfcf;
  }
  * { margin: 0; padding: 0; box-sizing: border-box; }
  html, body { width: 1200px; height: 900px; overflow: hidden; }
  body {
    background: radial-gradient(ellipse at 50% 40%, #f2f2f2 0%, var(--stage) 45%, var(--stage-edge) 100%);
    font-family: "Saira", sans-serif;
    position: relative;
  }
  .card {
    position: absolute;
    left: 280px;
    width: 640px;
    height: 366px;
    background: linear-gradient(160deg, var(--card) 0%, var(--card-deep) 100%);
    box-shadow: 0 14px 30px rgba(0,0,0,0.35);
  }
  .card--front { top: 50px; }
  .card--back { top: 470px; }

  /* front */
  .front-brand {
    position: absolute;
    left: 70px; top: 120px;
    display: flex; align-items: center; gap: 22px;
  }
  .brand-square { width: 56px; height: 56px; background: var(--green); }
  .brand-divider { width: 2px; height: 84px; background: var(--white); }
  .brand-name {
    color: var(--white);
    font-weight: 700;
    font-size: 40px;
    letter-spacing: 1px;
    line-height: 1;
    text-transform: uppercase;
  }
  .front-web {
    position: absolute;
    left: 0; right: 0; bottom: 40px;
    text-align: center;
    color: var(--green);
    font-weight: 600;
    font-size: 17px;
    letter-spacing: 6px;
  }

  /* back */
  .back-square {
    position: absolute;
    left: 60px; top: 200px;
    width: 110px; height: 110px;
    background: var(--green);
  }
  .back-divider {
    position: absolute;
    left: 228px; top: 26px;
    width: 2px; height: 290px;
    background: var(--white);
  }
  .back-brand {
    position: absolute;
    left: 258px; top: 36px;
    font-size: 34px;
  }
  .contact {
    position: absolute;
    left: 258px; top: 112px;
  }
  .contact-name { color: var(--white); font-weight: 600; font-size: 24px; line-height: 1.1; }
  .contact-title { color: var(--green); font-size: 15px; letter-spacing: 1.5px; margin-bottom: 16px; }
  .contact-list { list-style: none; }
  .contact-list li { color: var(--white); font-size: 15px; line-height: 1.45; }
  .contact-label { color: var(--green); font-weight: 600; display: inline-block; width: 22px; }
  .back-address {
    position: absolute;
    left: 200px; bottom: 30px;
    color: var(--green);
    font-size: 15px;
    letter-spacing: 0.5px;
    text-transform: uppercase;
  }
</style>
</head>
<body>
  <section class="card card--front" aria-label="Card front">
    <div class="front-brand">
      <span class="brand-square"></span>
      <span class="brand-divider"></span>
      <span class="brand-name">Dravetti Mining</span>
    </div>
    <p class="front-web">www.dravetti-example.com</p>
  </section>

  <section class="card card--back" aria-label="Card back">
    <span class="back-square"></span>
    <span class="back-divider"></span>
    <div class="brand-name back-brand">Dravetti Mining</div>
    <div class="contact">
      <p class="contact-name">Owen Pellsworth</p>
      <p class="contact-title">Managing Director</p>
      <ul class="contact-list">
        <li><span class="contact-label">P:</span> 972-555-0143</li>
        <li><span class="contact-label">E:</span> owen@dravetti-example.com</li>
        <li><span class="contact-label">W:</span> www.dravetti-example.com</li>
      </ul>
    </div>
    <p class="back-address">3157 Brantley #5 Dallas, TX 75209</p>
  </section>
</body>
</html>
```